Wattlebrook Legal: Sole Practitioner Law Firm seeking corporate branding drawing on unique bush setting

I need a logo, stationary and business card design for my law firm. I will be practising as a sole practitioner specialising in corporate, commercial, finance, migration and agriculture law. Having left my corporate job in the city and relocated our family to our farm in regional Western Australia, I would like the corporate design for my company to be crisp, stylish, concise and uncomplicated. The law firm is called "Wattlebrook Legal" because we have a colony of the endangered Carnaby Black Cockatoos living in the bush behind our homestead (which is also my office). I will travel to clients rather than have them visit me. I would like to see a stylised image of the bird with some Australian native bush included in the design, either as a background image on the back of the card. A separate brief has been created for the logo and stationary though I hope all 3 pieces of work will "marry". The final design should communicate clarity of vision, efficiency, compassion and solution/ outcome focused. I prefer to have the business cards printed on card with a bit of texture and substance. I will try not to use laminated card as I consider it feels "plastic and commoditised" which is inconsistent with the image and feel of the business I intend creating. Please see attached brief for further details of the design brief.

Target Market(s)

Agriculture and Horticulture companies, Farmers, Family offices and estates, banks, insurance companies, individuals wishing to migrate to Australia

Industry/Entity Type

Legal

Contact Information for Business Card

Harriet Lyle-Pemberton
LLB, BA (Hons), MCom.
Legal Practitioner and Director

WATTLEBROOK LEGAL PTY LTD
PO Box 726, Tindle Bay WA 6512
Ph: 0452 781906
Email: harrietlp@ferncastmail.com

Solicitor admitted to practice in the Upper Bench of Kestrel Shore, England and Wales, NSW, and Registered Practitioner of the Chief Bench of Marrowdale

Logo Text

WATTLEBROOK LEGAL: Client Focused Commercial Legal Solutions

Font styles to use
Other font styles liked:
• Verlag

Colors
ec1f27
fbee3d
9bcb3c
ffffff
1b1b1b
c4c4c4

Requirements
Must have
• A look and feel of quality, conservatism, adventure
Nice to have
• A stylised image of a Carnaby Cockatoo and Australian flora as a background image or design on the back of the card.
Should not have
• Clutter, cartoons

```html
<!DOCTYPE html>
<html lang="en">
<head>
<meta charset="utf-8">
<title>Wattlebrook Legal – Stationery Set</title>
<link rel="stylesheet" href="https://fonts.googleapis.com/css2?family=Cinzel:wght@500&family=Open+Sans:wght@400;600&family=Great+Vibes&display=swap">
<style>
  :root{
    --ink:#1b1b1b;
    --paper:#ffffff;
    --silver:#c4c4c4;
    --backdrop:#e9eaec;
    --text:#333333;
    --leaf:#55704a;
    --bloom:#d98a9a;
  }
  *{box-sizing:border-box;margin:0;padding:0}
  html,body{width:1200px;height:1200px;overflow:hidden}
  body{background:var(--backdrop);position:relative;font-family:"Open Sans",Arial,sans-serif;color:var(--text)}

  .brand{display:flex;align-items:center;gap:8px}
  .brand-dot{width:14px;height:14px;border-radius:50%;background:var(--ink);flex:none}
  .brand-text{display:flex;flex-direction:column;align-items:flex-end}
  .brand-name{font-family:"Cinzel",Georgia,serif;font-weight:500;color:var(--ink);letter-spacing:.5px;line-height:1;border-bottom:1px solid var(--ink);padding-bottom:2px;white-space:nowrap}
  .brand-sub{font-family:"Cinzel",Georgia,serif;font-size:8px;color:var(--ink);letter-spacing:1px;margin-top:2px}

  /* Letterhead */
  .letterhead{position:absolute;left:610px;top:40px;width:560px;height:792px;background:var(--paper);box-shadow:0 6px 18px rgba(0,0,0,.12)}
  .letterhead .brand{position:absolute;right:44px;top:48px}
  .letterhead .brand-name{font-size:22px}
  .recipient{position:absolute;left:44px;top:60px;font-size:9px;line-height:1.5}
  .letter-body{position:absolute;left:44px;right:44px;top:120px;font-size:9.5px;line-height:1.6;text-align:justify}
  .letter-body p{margin-bottom:12px}
  .closing{position:absolute;left:330px;top:560px;font-size:9px}
  .signature{font-family:"Great Vibes",cursive;font-size:24px;color:var(--ink);margin-top:2px}
  .footer-band{position:absolute;left:0;bottom:0;width:560px;height:130px}
  .footer-contact{position:absolute;left:0;right:0;bottom:36px;text-align:center;color:var(--paper);font-size:11px;letter-spacing:1px}

  /* Envelope */
  .envelope{position:absolute;left:40px;top:880px;width:540px;height:270px;background:var(--paper);box-shadow:0 6px 18px rgba(0,0,0,.12)}
  .envelope .brand{position:absolute;left:30px;top:30px}
  .envelope .brand-name{font-size:18px}
  .envelope-address{position:absolute;left:52px;top:82px;font-size:10px;color:var(--ink)}
  .envelope-band{position:absolute;left:0;right:0;top:175px;height:42px;background:var(--ink)}

  /* Business cards */
  .card{position:absolute;left:60px;width:420px;height:240px;box-shadow:0 6px 18px rgba(0,0,0,.14);overflow:hidden}
  .card-front{top:60px;background:var(--paper)}
  .flora-photo{position:absolute;inset:0;background:linear-gradient(135deg,#3e5a3a 0%,#6f8d5c 35%,var(--bloom) 55%,#5b7a4c 75%,#2f4630 100%)}
  .card-front .title-strip{position:absolute;left:0;right:0;top:92px;height:60px;background:rgba(255,255,255,.72);border-top:1px solid var(--paper);border-bottom:1px solid var(--paper);display:flex;align-items:center;justify-content:center}
  .card-front .brand-name{font-size:22px}

  .card-back{top:330px;background:var(--ink);color:var(--paper)}
  .card-back .details{position:absolute;left:0;right:0;top:28px;text-align:center}
  .card-back .brand-name{font-size:22px;color:var(--paper);border-color:var(--paper);display:inline-block}
  .card-back .brand-sub{color:var(--paper)}
  .holder-name{font-family:"Cinzel",Georgia,serif;font-size:15px;margin-top:14px;letter-spacing:.5px}
  .holder-quals,.holder-role{font-size:9px;color:var(--silver);margin-top:3px}
  .card-contact{position:absolute;left:24px;top:154px;font-size:9px;line-height:1.6;color:var(--silver)}
  .card-contact-right{left:auto;right:24px;text-align:right}
  .card-edge{position:absolute;left:0;bottom:0;width:420px;height:40px}
</style>
</head>
<body>

<section class="letterhead">
  <div class="brand">
    <span class="brand-dot"></span>
    <div class="brand-text">
      <span class="brand-name">Wattlebrook Legal</span>
      <span class="brand-sub">PTY LTD</span>
    </div>
  </div>
  <div class="recipient">To<br>The<br>Director;</div>
  <div class="letter-body">
    <p>Lorem Ipsum is simply dummy text of the printing and typesetting industry. Lorem Ipsum has been the industry's standard dummy text ever since the 1500s, when an unknown printer took a galley of type and scrambled it to make a type specimen book. It has survived not only five centuries, but also the leap into electronic typesetting, remaining essentially unchanged. It was popularised in the 1960s with the release of Transfertype sheets containing Lorem Ipsum passages, and more recently with desktop publishing software like Pagewright Studio including versions of Lorem Ipsum. Lorem Ipsum is simply dummy text of the printing and typesetting industry.</p>
    <p>Lorem Ipsum has been the industry's standard dummy text ever since the 1500s, when an unknown printer took a galley of type and scrambled it to make a type specimen book. It has survived not only five centuries, but also the leap into electronic typesetting, remaining essentially unchanged. It was popularised in the 1960s with the release of Transfertype sheets containing Lorem Ipsum passages and more recently with desktop publishing software like Pagewright Studio including versions of Lorem Ipsum. Lorem Ipsum is simply dummy text of the printing and typesetting industry.</p>
    <p>Lorem Ipsum has been the industry's standard dummy text ever since the 1500s, when an unknown printer took a galley of type and scrambled it to make a type specimen book. It has survived not only five centuries, but also the leap into electronic typesetting, remaining essentially unchanged. It was popularised in the 1960s with the release of Transfertype sheets containing Lorem Ipsum passages and more recently with desktop publishing software like Pagewright Studio including versions of Lorem Ipsum.</p>
  </div>
  <div class="closing">
    Thanking You
    <div class="signature">Alex Penrose</div>
  </div>
  <svg class="footer-band" viewBox="0 0 560 130" aria-hidden="true">
    <polygon points="0,0 92,0 110,22 450,22 468,0 560,0 560,130 0,130" fill="var(--ink)"/>
  </svg>
  <div class="footer-contact">0452 781906 | harrietlp@ferncastmail.com | PO Box 726, Tindle Bay WA 6512</div>
</section>

<section class="envelope">
  <div class="brand">
    <span class="brand-dot"></span>
    <div class="brand-text">
      <span class="brand-name">Wattlebrook Legal</span>
      <span class="brand-sub">PTY LTD</span>
    </div>
  </div>
  <div class="envelope-address">PO Box 726, Tindle Bay WA 6512</div>
  <div class="envelope-band"></div>
</section>

<section class="card card-front">
  <div class="flora-photo" role="img" aria-label="Photograph of pink native grevillea flowers among green bush foliage"></div>
  <div class="title-strip">
    <div class="brand">
      <span class="brand-dot"></span>
      <div class="brand-text">
        <span class="brand-name">Wattlebrook Legal</span>
        <span class="brand-sub">PTY LTD</span>
      </div>
    </div>
  </div>
</section>

<section class="card card-back">
  <div class="details">
    <span class="brand-name">Wattlebrook Legal</span>
    <div class="brand-sub">PTY LTD</div>
    <div class="holder-name">Harriet Lyle-Pemberton</div>
    <div class="holder-quals">LLB, BA (Hons), MCom.</div>
    <div class="holder-role">Legal Practitioner and Director</div>
  </div>
  <div class="card-contact">PO Box 726<br>Tindle Bay WA 6512</div>
  <div class="card-contact card-contact-right">Ph: 0452 781906<br>harrietlp@ferncastmail.com</div>
  <svg class="card-edge" viewBox="0 0 420 40" aria-hidden="true">
    <polygon points="0,2 60,2 72,14 348,14 360,2 420,2 420,40 0,40" fill="var(--silver)"/>
  </svg>
</section>

</body>
</html>
```